Business card design for global fintech startup

Verdell is a modern payments platform for the global insurance industry, serving international health, life, and travel insurers, MGAs, brokers, and partners.

We need a professional, premium business card for use at insurance conferences and executive meetings. The goal is to create a card that feels trustworthy, modern, and high-quality, while still being distinctive and memorable in a stack of business cards.

Target audience:
Senior insurance executives (VP, C-suite).

Design goals:
Clear, professional, and credible
Modern but not trendy
Premium and well-structured
Easy to read and practical for networking

Brand direction:
Brand-first (company over individual)
Follow existing brand guidelines where possible
Clean layout, strong hierarchy, excellent readability

Must include:
Name
Title
Company name (Verdell)
Logo
Email
Phone/Whatsapp
Website (www.joinverdell.com)
Tagline - Confidence in every payment

Materials & finish:
Open to designer recommendations for premium look and feel.

Please avoid:
Flashy or trendy startup styles
Generic insurance icons or clichés
Cluttered layouts or hard-to-read text

Deliverables:
Front and back business card, print-ready files.

Target Market(s)

Global Insurance executives

Industry/Entity Type

Fintech, Insurtech, Insurance, Financial Services

Contact Information for Business Card

Name Title Company name (Verdell) Logo Email Phone/Whatsapp Website (www.joinverdell.com) Tagline - Confidence in every payment

Font styles to use
Other font styles liked:
• See brand guidelines

Requirements
Nice to have
• something that stands out/makes us more memorable while still remaining professional
Should not have
• Please avoid: Flashy or trendy startup styles Generic insurance icons or clichés Cluttered layouts or hard-to-read text

```html
<!DOCTYPE html>
<html lang="en">
<head>
<meta charset="utf-8">
<title>Verdell Business Card</title>
<link rel="stylesheet" href="https://fonts.googleapis.com/css2?family=Montserrat:wght@400;500;600;700&display=swap">
<style>
  :root {
    --backdrop: #e4e4e4;
    --card-dark: #2b2b2b;
    --card-light: #f4f4f2;
    --ink: #1f1f1f;
    --ink-soft: #2e2e2e;
    --white: #f2f2f2;
    --map-tone: #383838;
    --map-tone-light: #444444;
    --violet: #6a2fd6;
    --blue: #2f86e0;
    --cyan: #27c7e6;
    --orange: #e8772a;
    --gold: #d9a83a;
  }
  * { box-sizing: border-box; margin: 0; padding: 0; }
  html, body { width: 1200px; height: 918px; overflow: hidden; }
  body {
    background: var(--backdrop);
    font-family: "Montserrat", sans-serif;
    display: flex;
    flex-direction: column;
    align-items: center;
    justify-content: center;
    gap: 56px;
  }
  .card {
    width: 560px;
    height: 320px;
    position: relative;
    border-radius: 2px;
    box-shadow: 0 10px 28px rgba(0,0,0,0.16);
    overflow: hidden;
  }
  /* Back side */
  .card-back { background: var(--card-dark); color: var(--white); }
  .card-back .world-map {
    position: absolute;
    left: 30px; top: 24px; width: 500px; height: 240px;
    background: radial-gradient(ellipse 60% 55% at 50% 48%, var(--map-tone-light) 0%, var(--map-tone) 50%, rgba(43,43,43,0) 100%);
  }
  .card-back .wordmark {
    position: absolute;
    left: 0; right: 0; top: 112px;
    display: flex; align-items: center; justify-content: center; gap: 16px;
  }
  .card-back .brand-dot {
    width: 26px; height: 26px; border-radius: 50%; background: var(--blue);
  }
  .card-back .brand-name {
    font-size: 50px; font-weight: 500; letter-spacing: 5px; text-transform: uppercase; line-height: 1;
  }
  .card-back .tagline {
    position: absolute; left: 0; right: 0; bottom: 44px;
    text-align: center; font-size: 11px; font-weight: 600;
    letter-spacing: 5px; text-transform: uppercase;
  }
  /* Front side */
  .card-front { background: var(--card-light); color: var(--ink); }
  .card-front .wordmark {
    position: absolute; right: 52px; top: 46px;
    display: flex; align-items: center; gap: 12px;
  }
  .card-front .brand-dot {
    width: 16px; height: 16px; border-radius: 50%; background: var(--blue);
  }
  .card-front .brand-name {
    font-size: 30px; font-weight: 500; letter-spacing: 3px; text-transform: uppercase; color: var(--ink); line-height: 1;
  }
  .card-front .person {
    position: absolute; left: 44px; top: 142px;
  }
  .card-front .person-name {
    font-size: 22px; font-weight: 700; letter-spacing: 1px; text-transform: uppercase; line-height: 1.2;
  }
  .card-front .person-title {
    font-size: 12px; font-weight: 500; margin-top: 2px; color: var(--ink-soft);
  }
  .card-front .spectrum-rule {
    position: absolute; left: 44px; right: 44px; top: 198px; height: 2px;
    background: linear-gradient(90deg, var(--cyan) 0%, var(--blue) 28%, var(--violet) 45%, var(--orange) 70%, var(--gold) 100%);
  }
  .card-front .contact-list {
    position: absolute; left: 44px; top: 216px; list-style: none;
    font-size: 12.5px; font-weight: 500; color: var(--ink-soft);
  }
  .card-front .contact-list li {
    display: flex; align-items: center; gap: 10px; line-height: 24px;
  }
  .card-front .contact-list svg { width: 12px; height: 12px; fill: var(--ink); }
</style>
</head>
<body>
  <section class="card card-back" aria-label="Card back">
    <div class="world-map" role="img" aria-label="Dotted world map in soft grey"></div>
    <div class="wordmark">
      <span class="brand-dot"></span>
      <span class="brand-name">Verdell</span>
    </div>
    <p class="tagline">Confidence in every payment</p>
  </section>

  <section class="card card-front" aria-label="Card front">
    <div class="wordmark">
      <span class="brand-dot"></span>
      <span class="brand-name">Verdell</span>
    </div>
    <div class="person">
      <h1 class="person-name">Marcus Hale</h1>
      <p class="person-title">Founder &amp; CEO</p>
    </div>
    <div class="spectrum-rule"></div>
    <ul class="contact-list">
      <li>
        <svg viewBox="0 0 24 24" aria-hidden="true"><path d="M6.6 10.8a15 15 0 0 0 6.6 6.6l2.2-2.2c.3-.3.7-.4 1-.2 1.1.4 2.3.6 3.6.6.6 0 1 .4 1 1V20c0 .6-.4 1-1 1A17 17 0 0 1 3 4c0-.6.4-1 1-1h3.5c.6 0 1 .4 1 1 0 1.3.2 2.5.6 3.6.1.3 0 .7-.2 1z"/></svg>
        (555) 014-2290
      </li>
      <li>
        <svg viewBox="0 0 24 24" aria-hidden="true"><path d="M2 5h20v14H2zm2 2v.5l8 5 8-5V7l-8 5z"/></svg>
        info@joinverdell.com
      </li>
      <li>
        <svg viewBox="0 0 24 24" aria-hidden="true"><path d="M12 2a10 10 0 1 0 0 20 10 10 0 0 0 0-20zm0 2c1 0 2.3 2 2.8 5H9.2C9.7 6 11 4 12 4zM4.3 11h3.8a17 17 0 0 0 0 2H4.3a8 8 0 0 1 0-2zm4.9 4h5.6c-.5 3-1.8 5-2.8 5s-2.3-2-2.8-5zm6.7-2a17 17 0 0 0 0-2h3.8a8 8 0 0 1 0 2z"/></svg>
        www.joinverdell.com
      </li>
    </ul>
  </section>
</body>
</html>
```